updating a virtual bank "pop-up" branch banner

we need to make this more modern looking. remove the woman please. make it look like 2022 and not 1980.

```html
<!DOCTYPE html>
<html lang="en">
<head>
<meta charset="utf-8">
<title>Nuvapay – Business Solutions Banner</title>
<link rel="stylesheet" href="https://fonts.googleapis.com/css2?family=Montserrat:wght@600;800&family=Poppins:wght@400;500;700&family=Open+Sans:wght@500&display=swap">
<style>
  :root {
    --page-bg: #eef5f9;
    --sky-top: #1b93db;
    --sky-bottom: #3fb8ef;
    --teal-deep: #0a7fa0;
    --teal-mid: #0b93b2;
    --white: #ffffff;
    --ink: #161616;
    --footer: #0a0a0b;
    --accent: #1187b2;
    --badge: #d9e3ea;
  }
  * { box-sizing: border-box; margin: 0; padding: 0; }
  html, body { width: 770px; height: 1200px; overflow: hidden; background: var(--page-bg); }
  .banner {
    position: absolute; left: 32px; top: 35px; width: 706px; height: 1130px;
    background: linear-gradient(180deg, var(--teal-deep) 40%, var(--teal-mid) 100%);
    box-shadow: 0 6px 28px rgba(30, 110, 150, 0.25);
    overflow: hidden;
    font-family: "Poppins", sans-serif; color: var(--white);
  }
  .hero-sky { position: absolute; left: 0; top: 0; width: 706px; height: 520px; }
  .brand-pill {
    position: absolute; left: 56px; top: 61px; width: 187px; height: 69px;
    background: var(--white); border-radius: 35px;
    display: flex; align-items: center; justify-content: center; gap: 8px;
  }
  .brand-dot { width: 12px; height: 12px; border-radius: 50%; background: var(--accent); }
  .brand-name { font-family: "Poppins", sans-serif; font-weight: 700; font-size: 26px; color: var(--ink); letter-spacing: 0.2px; }
  .headline {
    position: absolute; left: 53px; top: 212px; width: 360px;
    font-weight: 700; font-size: 35px; line-height: 42px; letter-spacing: -0.3px;
    white-space: nowrap;
  }
  .hero-art {
    position: absolute; left: 428px; top: 57px; width: 266px; height: 500px; border-radius: 18px;
    background: radial-gradient(ellipse at 70% 45%, #e9f3f8 0%, #a9d8f2 40%, rgba(80,175,230,0.35) 75%, rgba(60,160,220,0) 100%),
                linear-gradient(160deg, rgba(240,200,60,0.35) 0%, rgba(240,200,60,0) 45%);
  }
  .features { position: absolute; left: 0; top: 0; width: 100%; }
  .feature { position: absolute; width: 230px; }
  .feature-icon { width: 64px; height: 62px; display: block; }
  .feature-title {
    font-family: "Montserrat", sans-serif; font-weight: 600; font-size: 20px; letter-spacing: 0.3px;
    margin-top: 10px; line-height: 24px;
  }
  .feature-text { font-size: 15.5px; line-height: 19px; margin-top: 8px; font-weight: 400; }
  .partners {
    position: absolute; left: 0; top: 922px; width: 100%; height: 84px; background: var(--white);
  }
  .partners-label {
    position: absolute; left: 56px; top: 20px;
    font-family: "Montserrat", sans-serif; font-weight: 800; font-size: 21px; line-height: 23px;
    letter-spacing: -0.3px; color: var(--ink);
  }
  .partners-arrow { position: absolute; left: 196px; top: 17px; }
  .partner-badge { position: absolute; top: 24px; height: 36px; border-radius: 6px; background: var(--badge); }
  .contact-bar {
    position: absolute; left: 0; top: 1006px; width: 100%; height: 124px; background: var(--footer);
    font-family: "Open Sans", sans-serif; font-weight: 500; font-size: 17px;
  }
  .contact { position: absolute; top: 45px; display: flex; align-items: center; gap: 9px; }
  .contact-icon {
    width: 33px; height: 33px; border-radius: 50%; background: var(--accent);
    display: flex; align-items: center; justify-content: center;
  }
</style>
</head>
<body>
<main class="banner">
  <svg class="hero-sky" viewBox="0 0 706 520" aria-hidden="true">
    <defs>
      <linearGradient id="skyFill" x1="0" y1="0" x2="0" y2="1">
        <stop offset="0" stop-color="#1b93db"/>
        <stop offset="1" stop-color="#3fb8ef"/>
      </linearGradient>
    </defs>
    <path d="M0 0 H706 V514 H300 C200 514 120 450 0 370 Z" fill="url(#skyFill)"/>
  </svg>

  <div class="brand-pill"><span class="brand-dot"></span><span class="brand-name">nuvapay</span></div>

  <h1 class="headline">Grow your business<br>now with quick,<br>simple and easy<br>solutions.</h1>

  <div class="hero-art" role="img" aria-label="Smartphone showing a cash machine on screen, with banknotes and gold coins flying out and coin stacks beside it"></div>

  <section class="features">
    <div class="feature" style="left:56px;top:573px">
      <svg class="feature-icon" viewBox="0 0 64 62" fill="none" stroke="#fff" stroke-width="2.2" stroke-linejoin="round" stroke-linecap="round">
        <rect x="4" y="2" width="26" height="52" rx="4"/><rect x="8" y="8" width="18" height="12" rx="1"/>
        <path d="M9 28h4M17 28h4M9 36h4M17 36h4M9 44h4M17 44h4"/>
        <path d="M26 30l14-12 10 8-10 14-8 6M40 40l10 20"/>
      </svg>
      <div class="feature-title">SOFT POS</div>
      <div class="feature-text">Flexibility to get<br>payments</div>
    </div>
    <div class="feature" style="left:246px;top:573px">
      <svg class="feature-icon" viewBox="0 0 64 62" fill="none" stroke="#fff" stroke-width="2.2" stroke-linejoin="round" stroke-linecap="round">
        <rect x="14" y="2" width="30" height="56" rx="4"/><path d="M24 52h10"/>
        <circle cx="13" cy="28" r="10"/><path d="M13 22v12M16 24h-4a2 2 0 0 0 0 4h2a2 2 0 0 1 0 4h-4"/>
        <path d="M34 20h26l-4 16H38zM40 44a2 2 0 1 0 .1 0M54 44a2 2 0 1 0 .1 0"/>
      </svg>
      <div class="feature-title">E-COMMERCE</div>
      <div class="feature-text">Integrate safe &amp; secure<br>payment gateway</div>
    </div>
    <div class="feature" style="left:486px;top:573px">
      <svg class="feature-icon" viewBox="0 0 64 62" fill="none" stroke="#fff" stroke-width="2.2" stroke-linejoin="round" stroke-linecap="round">
        <rect x="18" y="26" width="44" height="30" rx="2"/><circle cx="40" cy="41" r="6"/>
        <path d="M2 46h20M2 52h20M2 58h20M6 40h14"/><path d="M6 30l14-12 10 6 22-20M44 4h8v8"/>
      </svg>
      <div class="feature-title">PAYROLL &amp; TAX</div>
      <div class="feature-text">Payroll and automated<br>business tax filling</div>
    </div>

    <div class="feature" style="left:56px;top:745px">
      <svg class="feature-icon" viewBox="0 0 64 62" fill="none" stroke="#fff" stroke-width="2.2" stroke-linejoin="round" stroke-linecap="round">
        <rect x="2" y="2" width="30" height="56" rx="4"/><rect x="7" y="7" width="20" height="14" rx="1"/>
        <path d="M11 14l4 4 7-7M9 30h3M16 30h3M23 30h3M9 38h3M16 38h3M23 38h3M9 46h3M16 46h3M23 46h3"/>
        <rect x="38" y="20" width="18" height="38" rx="3"/><path d="M41 12a14 14 0 0 1 12 0M44 16a7 7 0 0 1 6 0"/>
      </svg>
      <div class="feature-title">SMART POS</div>
      <div class="feature-text">Accept payment<br>at ease</div>
    </div>
    <div class="feature" style="left:246px;top:745px">
      <svg class="feature-icon" viewBox="0 0 64 62" fill="none" stroke="#fff" stroke-width="2.2" stroke-linejoin="round" stroke-linecap="round">
        <path d="M40 24V4H4v50h24"/><path d="M10 14h18M10 24h20M10 34h14M10 44h14"/>
        <path d="M46 28l14 5v10c0 9-6 14-14 17-8-3-14-8-14-17V33z"/><path d="M40 44l5 5 8-9"/>
      </svg>
      <div class="feature-title">INSURANCE</div>
      <div class="feature-text">Save big on insurance</div>
    </div>
    <div class="feature" style="left:486px;top:745px">
      <svg class="feature-icon" viewBox="0 0 64 62" fill="none" stroke="#fff" stroke-width="2.2" stroke-linejoin="round" stroke-linecap="round">
        <circle cx="52" cy="14" r="10"/><path d="M52 8v6h5"/>
        <path d="M26 8h10l-3 6c8 4 12 12 12 18 0 6-6 10-14 10s-14-4-14-10c0-6 4-14 12-18z"/>
        <path d="M31 22v14M34 24h-4a2 2 0 0 0 0 4h2a2 2 0 0 1 0 4h-4"/>
        <path d="M2 52l8-6h12c4 0 4 4 0 4h-8M14 50h14l12-6c3-1 4 3 1 4L26 58H10"/>
      </svg>
      <div class="feature-title">LOANS</div>
      <div class="feature-text">Get easy business<br>Loans</div>
    </div>
  </section>

  <section class="partners">
    <div class="partners-label">TRUSTED<br>PARTNERS</div>
    <svg class="partners-arrow" width="45" height="51" viewBox="0 0 45 51" aria-hidden="true"><path d="M0 0L45 25.5 0 51z" fill="#1187b2"/></svg>
    <span class="partner-badge" style="left:266px;width:52px;border-radius:18px"></span>
    <span class="partner-badge" style="left:348px;width:58px"></span>
    <span class="partner-badge" style="left:438px;top:14px;width:56px;height:56px;border-radius:2px"></span>
    <span class="partner-badge" style="left:526px;width:58px"></span>
    <span class="partner-badge" style="left:612px;width:62px"></span>
  </section>

  <footer class="contact-bar">
    <div class="contact" style="left:35px">
      <span class="contact-icon"><svg width="16" height="16" viewBox="0 0 24 24"><path d="M6.6 10.8a15 15 0 0 0 6.6 6.6l2.2-2.2a1 1 0 0 1 1-.25 11.4 11.4 0 0 0 3.6.57 1 1 0 0 1 1 1V20a1 1 0 0 1-1 1A17 17 0 0 1 3 4a1 1 0 0 1 1-1h3.5a1 1 0 0 1 1 1c0 1.250.2 2.45.57 3.57a1 1 0 0 1-.25 1z" fill="#fff"/></svg></span>
      <span>+91 8000 123 456</span>
    </div>
    <div class="contact" style="left:237px">
      <span class="contact-icon"><svg width="18" height="14" viewBox="0 0 18 14"><rect x="1" y="1" width="16" height="12" rx="1.5" fill="#fff"/><path d="M1.5 2l7.5 6 7.5-6" fill="none" stroke="#1187b2" stroke-width="1.5"/></svg></span>
      <span>support@nuvapay.com</span>
    </div>
    <div class="contact" style="left:480px">
      <span class="contact-icon"><svg width="18" height="18" viewBox="0 0 20 20" fill="none" stroke="#fff" stroke-width="1.6"><circle cx="10" cy="10" r="8"/><ellipse cx="10" cy="10" rx="3.5" ry="8"/><path d="M2 10h16M3.5 6h13M3.5 14h13"/></svg></span>
      <span>www.nuvapay.com</span>
    </div>
  </footer>
</main>
</body>
</html>
```